Pinecrest Renovations - Get the creative juices going!!

Pinecrest does not do the actual renovation work. The company provides high end project management of renovation (primarily residential - with an eye toward commercial) The renovation work could look very different between projects. This company manages the work of contractors, architects and interior designers (either subcontracted directly by Pinecrest or hired by the client and entrusted to Pinecrest to manage). Clients are high end in the economic scale and the card needs to have a high end feel to it.

The owner is female, but the audience will be heavily slanted male. It should not be a "feminine" or "masculine" looking card. If anything, slant more on the masculine side. Clean, simple, yet creative and artistically appealing. The card design should complement and in no way compete with the logo.

When people think of our company: trust, integrity, dynamic, limitless possibilities, transition, energy, creative. We plan to expand in the future to be international.

There will also be a contest running for stationary. Please check that section, as well.

***Black is 80-90 percent black. Not stark black

Tight timeline. Needs cards printed quickly!

Residential

```html
<!DOCTYPE html>
<html lang="en">
<head>
<meta charset="utf-8">
<title>Pinecrest Renovations – Business Card</title>
<link rel="stylesheet" href="https://fonts.googleapis.com/css2?family=Libre+Baskerville:ital,wght@0,400;1,400&display=swap">
<style>
  :root {
    --paper: #ffffff;
    --teal: #0aa79f;
    --ink: #413f42;
    --brand-white: #ffffff;
  }
  html, body {
    margin: 0;
    padding: 0;
    width: 1200px;
    height: 702px;
    overflow: hidden;
    background: var(--paper);
  }
  .card {
    position: relative;
    width: 1200px;
    height: 702px;
    font-family: "Libre Baskerville", Baskerville, Georgia, serif;
    color: var(--ink);
  }
  .card-face {
    position: absolute;
    left: 22px;
    top: 22px;
    width: 1158px;
    height: 658px;
    border-radius: 46px;
    background: var(--teal);
  }
  .card-frame {
    position: absolute;
    left: 41px;
    top: 41px;
    width: 1121px;
    height: 622px;
    box-sizing: border-box;
    border: 4px solid var(--ink);
    border-radius: 44px;
  }
  .contact-block {
    position: absolute;
    right: 122px;
    text-align: right;
    margin: 0;
    white-space: nowrap;
  }
  .person-name {
    top: 130px;
    font-size: 60px;
    line-height: 66px;
    font-weight: 400;
  }
  .person-title {
    top: 200px;
    font-size: 36px;
    line-height: 42px;
    font-style: italic;
  }
  .contact-lines {
    top: 314px;
    list-style: none;
    padding: 0;
    font-size: 54px;
    line-height: 66px;
  }
  .brand-mark {
    position: absolute;
    left: 252px;
    top: 430px;
    width: 118px;
    height: 118px;
    box-sizing: border-box;
    border: 4px solid var(--brand-white);
  }
  .brand-name {
    position: absolute;
    left: 70px;
    top: 582px;
    margin: 0;
    font-size: 31px;
    line-height: 38px;
    font-weight: 400;
    color: var(--brand-white);
    white-space: nowrap;
  }
</style>
</head>
<body>
  <main class="card">
    <div class="card-face"></div>
    <div class="card-frame"></div>

    <h1 class="contact-block person-name">NAME</h1>
    <p class="contact-block person-title">TITLE</p>

    <ul class="contact-block contact-lines">
      <li>NUMBER</li>
      <li>ADDRESS</li>
      <li>EMAIL</li>
      <li>WEB</li>
    </ul>

    <div class="brand-mark" aria-hidden="true"></div>
    <p class="brand-name">PINECREST RENOVATIONS</p>
  </main>
</body>
</html>
```